A spanish dental office Ads

We need a small poster sized Ads in Spanish, which has information as shown in the attached newspaper ads, please also add in office hour information as shown on the website(http://harborlanedentalcare.com/). Some other info could also be included, such as we provide broad range of dental services for both adult and children. practice logo was attached, the background of the ads do not need to be red.

Industry/Entity Type

Dental

```html
<!DOCTYPE html>
<html lang="es">
<head>
<meta charset="utf-8">
<title>Harbor Lane Dental Care – Anuncio</title>
<link rel="stylesheet" href="https://fonts.googleapis.com/css2?family=Fira+Sans+Extra+Condensed:wght@500;600&family=Open+Sans:wght@400;600;700&display=swap">
<style>
:root{
  --blue:#244d87;
  --yellow:#fccc00;
  --orange:#f44308;
  --white:#ffffff;
  --stage:#e4e4e4;
  --photo-light:#eef2f7;
  --photo-mid:#c8d5e6;
}
*{margin:0;padding:0;box-sizing:border-box}
html,body{width:1200px;height:1200px;overflow:hidden;background:var(--stage)}
.poster{position:absolute;left:199px;top:32px;width:853px;height:1208px;transform:scale(.94);transform-origin:0 0;overflow:hidden;background:var(--white);font-family:"Open Sans",sans-serif}
.poster > *{position:absolute;white-space:nowrap}
.photo{left:0;top:120px;width:853px;height:600px;background:linear-gradient(100deg,var(--photo-mid) 0%,var(--photo-light) 45%,#e4dcd3 75%,var(--photo-mid) 100%)}
.shapes{left:0;top:0;width:853px;height:1208px}
.cond{font-family:"Fira Sans Extra Condensed",sans-serif;font-weight:600}

.brand{left:22px;top:70px;display:flex;align-items:center;gap:14px;color:var(--white);font-weight:700;font-size:27px;letter-spacing:.5px;line-height:1.05}
.brand-dot{width:62px;height:62px;border-radius:50%;border:3px solid var(--white)}
.tagline{left:451px;top:25px;width:380px;height:47px;line-height:47px;text-align:center;color:var(--blue);font-size:40px}
.phone{left:506px;top:76px;font-size:60px;line-height:64px;color:var(--white)}
.assistant{left:451px;top:137px;font-size:30px;line-height:38px;color:var(--white);letter-spacing:.3px}

.offer{left:538px;top:538px;width:260px;text-align:center;color:var(--white)}
.offer-title{color:var(--yellow);font-size:56px;line-height:62px}
.offer-text{font-size:24px;line-height:29px;font-weight:500}

.price-label{left:24px;color:var(--blue);font-weight:700;font-size:22px;line-height:25px}
.price{width:170px;text-align:center;color:var(--blue);font-size:68px;line-height:70px}
.price sup{font-size:36px;vertical-align:22px}

.hours{left:456px;top:832px;width:372px;height:128px;border:2px solid var(--white)}
.hours-title{left:519px;top:806px;width:246px;text-align:center;background:var(--orange);color:var(--yellow);font-size:38px;line-height:50px}
.hours-table{left:483px;top:855px;width:318px;border-collapse:collapse;color:var(--white)}
.hours-table td{height:22px;padding:0 3px;font-size:15px;line-height:22px}
.hours-table tr:nth-child(even){background:var(--blue)}
.hours-table .time{font-family:"Fira Sans Extra Condensed",sans-serif;font-weight:600;font-size:17px;text-align:right}

.services{left:75px;top:978px;width:698px;height:57px;line-height:57px;text-align:center;color:var(--yellow);font-size:24px;font-weight:500}
.insurance{left:115px;top:1045px;color:var(--blue);font-weight:700;font-size:18px;line-height:26px}
.open-days{left:444px;top:1050px;color:var(--orange);font-size:30px;line-height:36px;font-weight:500}
.address{left:82px;top:1110px;width:740px;color:var(--white);font-size:27px;line-height:40px;font-weight:500}
.web,.mail{top:1160px;color:var(--orange);font-size:27px;line-height:40px;font-weight:500}
.web{left:90px;width:330px}
.mail{left:485px}
</style>
</head>
<body>
<div class="poster">
  <div class="photo" role="img" aria-label="Fotografía: paciente sonriente en el sillón dental atendida por un dentista"></div>

  <svg class="shapes" viewBox="0 0 853 1208" aria-hidden="true">
    <path d="M0,0 H853 V200 Q430,330 0,185 Z" fill="var(--blue)"/>
    <path d="M0,0 H853 V182 Q430,305 0,168 Z" fill="var(--yellow)"/>
    <path d="M0,0 H853 V166 Q430,285 0,150 Z" fill="var(--blue)"/>
    <line x1="426" y1="40" x2="426" y2="190" stroke="var(--white)" stroke-width="1.5" opacity=".7"/>
    <polygon points="451,25 831,25 818,48 831,72 451,72 464,48" fill="var(--yellow)"/>
    <circle cx="474" cy="108" r="24" fill="var(--yellow)"/>
    <circle cx="474" cy="108" r="19" fill="none" stroke="var(--blue)" stroke-width="2"/>
    <path d="M465,98 l5,-3 4,7 -3,3 q2,5 6,7 l3,-3 7,4 -3,5 q-10,2 -19,-20 z" fill="var(--blue)"/>
    <path d="M0,655 Q320,740 853,555 V1208 H0 Z" fill="var(--blue)"/>
    <path d="M0,675 Q320,758 853,590 V1208 H0 Z" fill="var(--yellow)"/>
    <path d="M0,695 Q320,775 853,622 V1208 H0 Z" fill="var(--orange)"/>
    <polygon transform="translate(668,643)" fill="var(--blue)" stroke="var(--white)" stroke-width="3"
      points="160,0 122.6,24.4 147.8,61.3 103.9,69.5 113.1,113.1 69.5,103.9 61.3,147.8 24.4,122.6 0,160 -24.4,122.6 -61.3,147.8 -69.5,103.9 -113.1,113.1 -103.9,69.5 -147.8,61.3 -122.6,24.4 -160,0 -122.6,-24.4 -147.8,-61.3 -103.9,-69.5 -113.1,-113.1 -69.5,-103.9 -61.3,-147.8 -24.4,-122.6 0,-160 24.4,-122.6 61.3,-147.8 69.5,-103.9 113.1,-113.1 103.9,-69.5 147.8,-61.3 122.6,-24.4"/>
    <rect x="12" y="768" width="359" height="87" fill="var(--yellow)" stroke="#f08a00" stroke-width="2" stroke-dasharray="3 3"/>
    <polygon points="216,770 385,770 385,838 232,838" fill="var(--white)"/>
    <rect x="12" y="863" width="359" height="89" fill="var(--yellow)" stroke="#f08a00" stroke-width="2" stroke-dasharray="3 3"/>
    <polygon points="232,865 385,865 385,935 216,935" fill="var(--white)"/>
    <rect x="0" y="978" width="853" height="130" fill="var(--yellow)"/>
    <polygon points="75,978 773,978 757,1035 97,1035" fill="var(--blue)"/>
    <line x1="426" y1="1045" x2="426" y2="1093" stroke="var(--orange)" stroke-width="1.5"/>
    <rect x="0" y="1108" width="853" height="44" fill="var(--blue)"/>
    <rect x="0" y="1152" width="853" height="56" fill="var(--yellow)"/>
    <path d="M63,1117 a9,9 0 0 1 9,9 c0,7 -9,16 -9,16 c0,0 -9,-9 -9,-16 a9,9 0 0 1 9,-9 z" fill="var(--yellow)"/>
    <circle cx="63" cy="1126" r="3.5" fill="var(--blue)"/>
    <g fill="none" stroke="var(--blue)" stroke-width="1.8">
      <circle cx="64" cy="1180" r="15"/>
      <circle cx="64" cy="1180" r="11"/>
      <ellipse cx="64" cy="1180" rx="5" ry="11"/>
      <line x1="53" y1="1180" x2="75" y2="1180"/>
      <line x1="55" y1="1174" x2="73" y2="1174"/>
      <line x1="55" y1="1186" x2="73" y2="1186"/>
    </g>
    <line x1="428" y1="1163" x2="428" y2="1198" stroke="var(--blue)" stroke-width="1.5"/>
    <g fill="none" stroke="var(--blue)" stroke-width="1.8">
      <circle cx="457" cy="1180" r="15"/>
      <rect x="448" y="1174" width="18" height="12"/>
      <polyline points="448,1174 457,1181 466,1174"/>
    </g>
  </svg>

  <div class="brand"><span class="brand-dot"></span><span>HARBOR LANE<br>DENTAL CARE</span></div>
  <div class="tagline cond">HABLAMOS ESPAÑOL</div>
  <div class="phone cond">555-214-0187</div>
  <div class="assistant">Lucia Asistente Hispana</div>

  <div class="offer">
    <div class="offer-title cond">GRATIS</div>
    <div class="offer-text cond">nuevos<br>pacientescon<br>seguro reciben de<br>regalo un cepillo<br>eléctrico</div>
  </div>

  <div class="price-label" style="top:785px">Blanqueo<br>profesional</div>
  <div class="price cond" style="left:210px;top:768px"><sup>$</sup>99</div>
  <div class="price-label" style="top:880px;left:21px">Diagnostico,<br>rayos y limpieza</div>
  <div class="price cond" style="left:210px;top:864px"><sup>$</sup>79</div>

  <div class="hours"></div>
  <div class="hours-title cond">Office Hours</div>
  <table class="hours-table">
    <tr><td>Monday - Wednesday</td><td class="time">08:00 am – 5:00 pm</td></tr>
    <tr><td>Thursday</td><td class="time">08:00 am – 7:00 pm</td></tr>
    <tr><td>Friday</td><td class="time">08:00 am – 5:00 pm</td></tr>
    <tr><td>Saturday</td><td class="time">08:00 am – 3:00 pm</td></tr>
  </table>

  <div class="services cond">we provide broad range of dental services for both adult and children.</div>
  <div class="insurance">Aceptamos la mayoria de los<br>seguros y medicaid</div>
  <div class="open-days cond">Abierto de lunes a sabados</div>
  <div class="address cond">2150 Meadow Ave. Suite 106, Dover, NC 27000 (salida 276 de la 40)</div>
  <div class="web cond">www.harborlanedentalcare.com</div>
  <div class="mail cond">hldentalcare@example.com</div>
</div>
</body>
</html>
```